CD Cover for Professional Metaphysical Album

I actually have two Meditation albums ready to go out digitally. Needs somewhat consistent appearance for both as they are from same author - however audio themes are very different. Prior attempts with 5 other designers elsewhere failed to turn up professional level results. Im happy to discuss producing immediately a 2nd album as I see CD 1 succeeding.

CD 1 Title needs to read Quiet Harbor Reflections
My name needs to appear at bottom I presume .. Martin Osgood
*I am fairly certain of how I'd like cover to appear - white horizontal rectangular area above/below image where text is inserted. I have some examples attached to consider/inspire you. Willing to go outside the box in thinking.

CD 1 (image: AmberTide Awakening-Lorimesa-300DPI) is the MASTER IMAGE to work from.

This project we already know will be purchased mostly by women, if such matters.

Target Market(s)

metaphysical, spiritual, meditation, metaphysics

Industry/Entity Type

Religious

Colors

Designer to choose colors to be used in the design.

Requirements
Must have
• Title : Quiet Harbor Reflections
• Author name: Martin Osgood
• White header footer preferred strongly but will consider options
• Eye catching fonts but im poor with picking such! Need your expertise on font color also!
Nice to have
• unsure
Should not have
• unsure

```html
<!DOCTYPE html>
<html lang="en">
<head>
<meta charset="utf-8">
<title>Quiet Harbor Reflections – Martin Osgood</title>
<link rel="stylesheet" href="https://fonts.googleapis.com/css2?family=Federo&family=Pinyon+Script&display=swap">
<style>
  :root {
    --deep-blue: #1a2f8f;
    --ocean-blue: #1f6fd6;
    --aqua: #3fe0f2;
    --violet: #7a2fc4;
    --magenta: #e23fd6;
    --rose: #ff3d8c;
    --amber: #ffa32a;
    --text-white: #fbf6ff;
  }
  html, body {
    margin: 0;
    padding: 0;
    width: 1200px;
    height: 1200px;
    overflow: hidden;
    background: #ffffff;
  }
  .album-cover {
    position: relative;
    width: 1200px;
    height: 1200px;
    overflow: hidden;
  }
  .cover-artwork {
    position: absolute;
    inset: 0;
    background:
      radial-gradient(circle at 50% 53%, var(--amber) 0%, var(--rose) 14%, var(--magenta) 26%, var(--violet) 37%, rgba(122,47,196,0) 39%),
      radial-gradient(circle at 50% 53%, rgba(230,210,255,0.9) 38.5%, rgba(230,210,255,0) 40.5%),
      radial-gradient(ellipse at 50% 50%, #b23ad8 0%, #5a3bc4 40%, rgba(31,111,214,0) 65%),
      linear-gradient(90deg, var(--aqua) 0%, var(--ocean-blue) 18%, var(--deep-blue) 50%, var(--ocean-blue) 82%, var(--aqua) 100%);
  }
  .album-title {
    position: absolute;
    top: 62px;
    left: 0;
    right: 0;
    margin: 0;
    text-align: center;
    font-family: "Federo", sans-serif;
    font-weight: 400;
    font-size: 68px;
    letter-spacing: 1px;
    color: var(--text-white);
    text-shadow: 0 0 12px rgba(120, 40, 160, 0.6);
  }
  .album-artist {
    position: absolute;
    bottom: 50px;
    left: 0;
    right: 0;
    margin: 0;
    text-align: center;
    font-family: "Pinyon Script", cursive;
    font-weight: 400;
    font-size: 92px;
    color: var(--text-white);
    text-shadow: 0 0 10px rgba(40, 20, 120, 0.6);
  }
</style>
</head>
<body>
  <main class="album-cover">
    <div class="cover-artwork" role="img" aria-label="Luminous illustration of a seated meditating silhouette inside a glowing violet circle of sacred geometry, radiating amber and magenta light over flowing blue and aqua energy waves"></div>
    <h1 class="album-title">Quiet Harbor Reflections</h1>
    <p class="album-artist">Martin Osgood</p>
  </main>
</body>
</html>
```